Wordpress template for a mens-choire webpage

Task is to design a Wordpress template for an 98 years old KALJU MENS CHOIRE webpage.
Design should involve details from the attached files, choire logo and the colors of the choire flag: in horizontal orientation bright sky-blue, white, bright grass-green.
Designer signature is allowed to be added to the template, with country of origin.

Reason: Deadline extended 2 days (until 2. March 2014) to accommodate designers creativity.

Thank you everyone for your great designs!
Our project has now entered into a voting and decision phase until 14th of March 2014 (included).

```html
<!DOCTYPE html>
<html lang="en">
<head>
<meta charset="utf-8">
<title>Kalju Mens Choire</title>
<link href="https://fonts.googleapis.com/css2?family=Roboto:ital,wght@0,300;0,400;0,500;1,300&display=swap" rel="stylesheet">
<style>
:root{
  --green-dark:#0f3a16;
  --green:#2f8a2a;
  --green-mid:#1c5e22;
  --page:#ececec;
  --band:#dedede;
  --text:#1c1c1c;
  --muted:#777;
  --red:#b01e1e;
  --red-dark:#7e1010;
  --blue-dark:#0a2a52;
  --blue:#1d62a6;
  --white:#fff;
}
*{margin:0;padding:0;box-sizing:border-box}
html,body{width:732px;height:1200px;overflow:hidden}
body{font-family:"Roboto",sans-serif;color:var(--text);background:var(--page);position:relative}
.abs{position:absolute}
.header{left:0;top:0;width:732px;height:400px;background:radial-gradient(ellipse at 50% 20%,#5f9a5a 0%,var(--green) 35%,var(--green-mid) 70%,var(--green-dark) 100%)}
.slant-top{left:0;top:350px;width:732px;height:60px}
.brand-mark{left:58px;top:12px;width:62px;height:62px;border-radius:50%;background:#f4f1e6;border:3px solid #c9a64a}
.brand-name{left:132px;top:29px;color:var(--white);font-size:22px;font-weight:500;line-height:1;letter-spacing:.3px}
.brand-sub{left:134px;top:55px;color:#e8efe6;font-size:16px;font-weight:300;letter-spacing:.3px}
.search{left:474px;top:16px;width:203px;height:26px;background:var(--white);border-radius:4px;font-size:10px;color:#bbb;padding:7px 8px}
.search svg{position:absolute;right:6px;top:6px}
.nav{left:353px;top:57px;display:flex;gap:17px;font-size:12.5px;color:var(--white)}
.nav span{padding-bottom:4px}
.nav .active{border-bottom:1px solid #fff}
.nav-rule{left:353px;top:81px;width:324px;border-top:1px dotted rgba(255,255,255,.4)}
.slide{left:55px;top:103px;width:622px;height:248px;background:linear-gradient(180deg,#1a1a1a 0%,#3a2a2e 45%,#8a5a38 80%,#b07a48 100%)}
.caption{left:55px;top:290px;width:249px;height:45px;background:rgba(0,0,0,.75);color:var(--white);font-size:13.5px;padding:15px 23px}
.dots{left:55px;top:359px;display:flex;gap:4px}
.dots i{width:11px;height:11px;border-radius:50%;background:#111;border:1px solid #555}
.dots i.on{background:#fff;border:2px solid #111;box-shadow:0 0 0 1px #fff}
h2{font-weight:400;font-size:17px;letter-spacing:.2px;position:absolute;color:#111}
.rule{position:absolute;height:3px;border-top:1px dotted #999;border-bottom:1px dotted #999}
.video{left:55px;top:467px;width:190px;height:133px;background:var(--white);box-shadow:0 0 3px rgba(0,0,0,.3);padding:6px}
.video .shot{width:100%;height:100%;background:linear-gradient(135deg,#3a3a2a,#1a1a1a 60%,#4a4a4a)}
.video svg{position:absolute;left:70px;top:42px}
.small-title{font-size:8.5px;color:#222}
.small-note{font-size:7.3px;color:#666;font-style:italic;font-weight:300;line-height:1.25}
.arrows{left:222px;top:606px;font-size:12px;color:#555;letter-spacing:3px}
.news{left:57px;width:190px}
.news .thumb{position:absolute;left:0;top:0;width:42px;height:37px;background:linear-gradient(135deg,#6a5a48,#2a2a2a)}
.news .body{position:absolute;left:49px;top:0}
.date{font-size:8.5px;color:var(--red)}
.more{font-size:8.5px;color:#222}
.welcome{left:281px;top:468px;width:398px;font-size:9.3px;line-height:15.5px;color:var(--muted);font-weight:300}
.welcome p{margin-bottom:15.5px}
.welcome a{color:var(--red);text-decoration:none}
.event{width:180px;height:64px}
.event .thumb{position:absolute;left:0;top:0;width:66px;height:61px}
.event .body{position:absolute;left:75px;top:0;width:110px}
.event .t{font-size:8.5px;color:var(--red)}
.event .d{font-size:8px;color:#666;font-weight:300}
.event .x{font-size:7.6px;color:#777;font-weight:300;line-height:1.3;margin-top:3px}
.ev-sep{left:477px;top:755px;height:82px;border-left:1px solid #ccc}
.gallery{left:0;top:865px;width:732px;height:125px;background:var(--band)}
.gallery-tag{left:56px;top:893px;width:150px;height:74px}
.gallery-tag .k{position:absolute;left:12px;top:16px;font-size:8px;color:#f3d6d6;font-style:italic}
.gallery-tag .n{position:absolute;left:12px;top:28px;font-size:14px;color:var(--white)}
.g-thumb{top:888px;width:108px;height:83px;background:var(--white);box-shadow:0 0 3px rgba(0,0,0,.3);padding:4px}
.g-thumb div{width:100%;height:100%}
.footer{left:0;top:1000px;width:732px;height:200px;background:radial-gradient(ellipse at 55% 40%,var(--blue) 0%,#144a86 45%,var(--blue-dark) 100%)}
.f-nav{left:56px;top:1068px;display:flex;gap:8px;font-size:10px;color:var(--white)}
.f-copy{left:56px;top:1093px;font-size:10px;color:var(--white)}
.social{left:56px;top:1128px;display:flex;gap:6px}
.social i{width:26px;height:26px;border-radius:50%;background:#e9eef3;border:2px solid #9fb3c9}
.reach{right:58px;top:1067px;text-align:right;color:var(--white);font-size:11.5px}
.addr{right:58px;top:1089px;text-align:right;color:#e8eef6;font-size:10px;line-height:12.8px}
.contact{right:58px;top:1150px;text-align:right;color:#e8eef6;font-size:10px;line-height:12.8px}
</style>
</head>
<body>

<div class="abs header"></div>
<svg class="abs slant-top" width="732" height="60" viewBox="0 0 732 60" aria-hidden="true">
  <polygon points="0,34 732,4 732,60 0,60" fill="#cfcfcf"/>
  <polygon points="0,46 732,16 732,60 0,60" fill="var(--page)"/>
</svg>

<div class="abs brand-mark"></div>
<div class="abs brand-name">KALJU</div>
<div class="abs brand-sub">MENS CHOIRE</div>

<div class="abs search">Search
  <svg width="14" height="14" viewBox="0 0 14 14"><circle cx="5.5" cy="5.5" r="4" fill="none" stroke="#222" stroke-width="2"/><line x1="8.5" y1="8.5" x2="13" y2="13" stroke="#222" stroke-width="2.2"/></svg>
</div>
<nav class="abs nav"><span class="active">Home</span><span>About us</span><span>Services</span><span>Videos</span><span>Events</span><span>Contact</span></nav>
<div class="abs nav-rule"></div>

<div class="abs slide" role="img" aria-label="Photo of a young men's choir in striped blazers singing on stage with their conductor"></div>
<div class="abs caption">98 Years of Estonian Choire</div>
<div class="abs dots"><i class="on"></i><i></i><i></i><i></i><i></i></div>

<h2 style="left:56px;top:435px">LATEST VIDEO</h2>
<div class="abs video">
  <div class="shot" role="img" aria-label="Video still of a choir performing in a concert hall"></div>
  <svg width="42" height="42" viewBox="0 0 42 42" aria-hidden="true"><circle cx="21" cy="21" r="19" fill="#111" stroke="#fff" stroke-width="2.5"/><polygon points="16,11 31,21 16,31" fill="#fff"/></svg>
</div>
<div class="abs" style="left:55px;top:609px">
  <div class="small-title">Lorem ipsum dolor</div>
  <div class="small-note">sit amet, consectetur adipisicing elit,<br>sed do</div>
</div>
<div class="abs arrows">❮❯</div>
<div class="rule" style="left:56px;top:655px;width:189px"></div>

<h2 style="left:56px;top:682px">LATEST NEWS</h2>
<div class="abs news" style="top:715px;height:40px">
  <div class="thumb" role="img" aria-label="News photo of a conductor on stage"></div>
  <div class="body"><div class="date">Feb 1, 2014</div><div class="small-title">Lorem ipsum dolor</div><div class="small-note">sit amet, consectetur adipisicing elit,<br>sed do</div></div>
</div>
<div class="abs news" style="top:768px;height:40px">
  <div class="thumb" role="img" aria-label="News photo of choir singers"></div>
  <div class="body"><div class="date">Feb 1, 2014</div><div class="small-title">Lorem ipsum dolor</div><div class="small-note">sit amet, consectetur adipisicing elit,<br>sed do</div></div>
</div>
<div class="abs more" style="left:56px;top:826px">More News</div>
<div class="rule" style="left:56px;top:843px;width:189px"></div>

<h2 style="left:281px;top:435px">WELCOME TO OUR WEBSITE</h2>
<div class="abs welcome">
  <p>Lorem ipsum dolor sit amet, consectetur adipisicing elit, sed do eiusmod tempor incididunt ut labore et dolore magna aliqua. Ut enim ad minim veniam, quis nostrud exercitation ullamco laboris nisi ut aliquip ex ea commodo consequat. Duis aute irure dolor in reprehenderit in voluptate velit esse cillum dolore eu fugiat nulla pariatur. Excepteur sint occaecat cupidatat non proident, sunt in culpa qui officia deserunt mollit anim id est laborum.</p>
  <p>Lorem ipsum dolor sit amet, consectetur adipisicing elit, sed do eiusmod tempor incididunt ut labore et dolore magna aliqua. Ut enim ad minim veniam, quis nostrud exercitation ullamco laboris nisi ut aliquip ex ea commodo consequat. Duis aute irure dolor in reprehenderit riatur. Excepteur sint occaecat cupidatat non proident, sunt in culpa qui officia deserunt mollit anim id est laborum Lorem ipsum dolor sit amet, consectetur adipisicing elit, sed do eiusmod tempor incididunt ut labore et dolore magna aliqua. .</p>
  <p>Lorem ipsum dolor sit amet, consectetur adipisicing elit, sed do eiusmod tempor incididunt ut labore et dolore magna aliqua. . <a>More</a></p>
</div>
<div class="rule" style="left:281px;top:710px;width:397px"></div>

<h2 style="left:281px;top:731px">EVENTS</h2>
<div class="abs event" style="left:282px;top:760px">
  <div class="thumb" role="img" aria-label="Event photo of a choir with orchestra in a hall" style="background:linear-gradient(160deg,#c9b08a,#6a2a2a 60%,#2a2a3a)"></div>
  <div class="body"><div class="t">Lorem ipsum dolor</div><div class="d">21 Feb 2014</div><div class="x">Csit amet, consectetur adipi-sicing elit, sed do sit amet, consectetur adipisicing elit, sed do</div></div>
</div>
<div class="abs ev-sep"></div>
<div class="abs event" style="left:494px;top:760px">
  <div class="thumb" role="img" aria-label="Event photo of a choir in formal dress" style="background:linear-gradient(160deg,#8a6a4a,#2a2020 60%,#4a3a3a)"></div>
  <div class="body"><div class="t">Lorem ipsum dolor</div><div class="d">21 Feb 2014</div><div class="x">Csit amet, consectetur adipi-sicing elit, sed do sit amet, consectetur adipisicing elit, sed do</div></div>
</div>
<div class="rule" style="left:281px;top:843px;width:397px"></div>

<div class="abs gallery"></div>
<svg class="abs gallery-tag" width="150" height="74" viewBox="0 0 150 74" aria-hidden="true">
  <polygon points="0,0 124,0 150,37 124,74 0,74" fill="#fff"/>
  <polygon points="3,3 122,3 146,37 122,71 3,71" fill="var(--red-dark)"/>
  <circle cx="20" cy="55" r="7" fill="none" stroke="#d9a0a0" stroke-width="1.2"/>
  <path d="M23 55 H17 M19.5 52.5 L17 55 L19.5 57.5" stroke="#d9a0a0" stroke-width="1.2" fill="none"/>
  <circle cx="40" cy="55" r="7" fill="none" stroke="#fff" stroke-width="1.4"/>
  <path d="M37 55 H43 M40.5 52.5 L43 55 L40.5 57.5" stroke="#fff" stroke-width="1.4" fill="none"/>
</svg>
<div class="abs gallery-tag" style="pointer-events:none"><div class="k">Latest</div><div class="n">PHOTO GALLERY</div></div>
<div class="abs g-thumb" style="left:222px"><div role="img" aria-label="Gallery photo of a concert with grand piano" style="background:linear-gradient(150deg,#d8b878,#5a3a1a 55%,#1a1a1a)"></div></div>
<div class="abs g-thumb" style="left:338px"><div role="img" aria-label="Gallery photo of choir singers in a church" style="background:linear-gradient(150deg,#8a7a6a,#1a1a1a 55%,#3a3a3a)"></div></div>
<div class="abs g-thumb" style="left:454px"><div role="img" aria-label="Gallery photo of singers in traditional costume" style="background:linear-gradient(150deg,#9a8a7a,#2a1a1a 50%,#7a2a2a)"></div></div>
<div class="abs g-thumb" style="left:570px"><div role="img" aria-label="Gallery photo of a large choir in black and white" style="background:linear-gradient(150deg,#5a5a5a,#1a1a1a 50%,#c8c8c8)"></div></div>

<svg class="abs" style="left:0;top:990px" width="732" height="50" viewBox="0 0 732 50" aria-hidden="true">
  <rect width="732" height="50" fill="var(--page)"/>
  <polygon points="0,20 732,20 732,0 0,0" fill="var(--band)"/>
  <polygon points="0,50 0,40 732,10 732,50" fill="#cfcfcf"/>
</svg>
<svg class="abs" style="left:0;top:1000px;width:732px;height:200px" viewBox="0 0 732 200" aria-hidden="true">
  <defs><radialGradient id="fb" cx="55%" cy="40%" r="70%"><stop offset="0" stop-color="#1d62a6"/><stop offset=".45" stop-color="#144a86"/><stop offset="1" stop-color="#0a2a52"/></radialGradient></defs>
  <polygon points="0,40 732,12 732,200 0,200" fill="url(#fb)"/>
</svg>

<nav class="abs f-nav"><span>Home</span><span>About us</span><span>Services</span><span>Vidoes</span><span>Gallery</span><span>Events</span><span>Contact</span></nav>
<div class="abs f-copy">All Rights reserved Copyrights @ 2014</div>
<div class="abs social" aria-label="Social links"><i></i><i></i><i></i><i></i></div>

<div class="abs reach">REACH US</div>
<div class="abs addr">KALJU MEN CHOIRE<br>No.27, occaecat cupidatat<br>Non proident,<br>Suntin</div>
<div class="abs contact">Tel: 052 555 0143<br>Email: hello@kaljuchoir.example</div>

</body>
</html>
```